Tolvik Hearthline Website Images

We manufacture electric fireplaces and require images of our new product in various sizes.
We have 5 sizes of fireplace. A 36", 42", 50", 72" and a 100". However, the only image we currently have is for a 60", but need these same images to show the product in 36", 42", 50", 72" and 100". Therefore, a scale needs to be made so the images look different for each size of fireplace. The photos we already have show the fire with its different coloured flames.
We require:
1. Close up image showing all the different flame colours. Attached is an example of how it needs to look, but with our colours as per our images (EXAMPLE_flamecolourscloseup)
2. I have uploaded the images (S1-S16) which need to be scaled to show all sizes of the fireplace (36", 42", 50", 72", 100").
3. Image S12 with the dimensions of each size. Example attached (EXAMPLE_fireplacedimensions). Dimensions are as follows:
36" - 914 mm x 140 mm x 430 mm. 16.7 kg.
42" - 1060 mm x 140 mm x 430 mm. 19.5 kg.
50" - 1270 mm x 140 mm x 430 mm. 22.6 kg.
72" - 1829 mm x 140 mm x 430 mm. 35.5 kg.
100" - 2540 mm x 140 mm x 430 mm. 49.3 kg.
4. We also require the product highlights to be added like the attached example (EXAMPLE_fireplacehighlights) but with the new fireplace model image (S12).
5. We also require image and writing attached (EXAMPLE_heatoutput) with our image S12.
6. We also require image (new_purple) to be photoshopped with our new fireplace (image S11-S16).
Logos etc all attached too.
I hope this makes sense. Any questions, please ask :)

```html
<!DOCTYPE html>
<html lang="en">
<head>
<meta charset="UTF-8">
<title>Tolvik Hearthline – Dimensions</title>
<link rel="stylesheet" href="https://fonts.googleapis.com/css2?family=Oswald:wght@600;700&family=Roboto:wght@400;700;900&display=swap">
<style>
  :root {
    --bg: #e9e9ea;
    --bg-soft: #f3f3f4;
    --header: #2a2b2e;
    --header-deep: #1b1c1e;
    --accent: #f5b000;
    --accent-deep: #e08a00;
    --ink: #111111;
    --line: #3a3a3a;
    --frame: #0c0c0c;
    --frame-edge: #4a4a4a;
    --flame-dark: #120604;
    --flame-mid: #7a1c06;
    --flame-hot: #f06a10;
    --flame-bright: #ffc04a;
    --white: #ffffff;
  }
  * { box-sizing: border-box; margin: 0; padding: 0; }
  html, body { width: 745px; height: 1200px; overflow: hidden; }
  body {
    position: relative;
    background: radial-gradient(ellipse at 50% 45%, var(--bg-soft), var(--bg) 70%);
    font-family: "Roboto", Arial, sans-serif;
    color: var(--ink);
  }

  /* Header */
  .header {
    position: absolute; left: 0; top: 0; width: 745px; height: 100px;
    background: linear-gradient(180deg, var(--header) 0%, var(--header-deep) 100%);
  }
  .header__title {
    position: absolute; left: 22px; top: 44px;
    font-family: "Oswald", "Arial Narrow", sans-serif;
    font-weight: 700; font-size: 34px; letter-spacing: 1px;
    color: var(--accent);
    line-height: 1;
  }
  .header__stripes { position: absolute; left: 0; top: 100px; width: 745px; height: 18px; }
  .brand {
    position: absolute; left: 512px; top: 10px; width: 226px; height: 84px;
    background: var(--white);
    border: 3px solid var(--header-deep);
    display: flex; align-items: center; justify-content: center; gap: 10px;
  }
  .brand__mark { width: 12px; height: 12px; background: var(--header-deep); }
  .brand__name {
    font-family: "Roboto", Arial, sans-serif; font-weight: 900;
    font-size: 23px; color: var(--header-deep); line-height: 1.05;
    text-align: center;
  }

  /* Fireplace units */
  .unit { position: absolute; left: 0; width: 745px; }
  .unit__size {
    position: absolute; left: 75px; top: 0;
    width: var(--w); text-align: center;
    font-weight: 700; font-size: 25px; line-height: 1;
  }
  .unit__frame {
    position: absolute; left: 75px; top: 22px;
    width: var(--w); height: var(--h);
    background: var(--frame);
    border: 2px solid var(--frame-edge);
    padding: 5px;
  }
  .unit__flame {
    width: 100%; height: 100%;
    background:
      linear-gradient(0deg, var(--flame-bright) 0%, var(--flame-hot) 14%, rgba(240,106,16,0.55) 38%, rgba(122,28,6,0.35) 60%, transparent 80%),
      linear-gradient(180deg, var(--flame-dark), var(--flame-mid));
  }
  .dim-h {
    position: absolute; left: 75px; top: calc(22px + var(--h) + 8px);
    width: var(--w); height: 10px;
    border-left: 1px solid var(--line); border-right: 1px solid var(--line);
  }
  .dim-h::before {
    content: ""; position: absolute; left: 0; right: 0; top: 5px;
    border-top: 1px solid var(--line);
  }
  .dim-h__label {
    position: absolute; left: 0; right: 0; top: 11px;
    text-align: center; font-size: 10px;
  }
  .dim-v {
    position: absolute; left: 52px; top: 22px;
    width: 10px; height: var(--h);
    border-top: 1px solid var(--line); border-bottom: 1px solid var(--line);
  }
  .dim-v::before {
    content: ""; position: absolute; top: 0; bottom: 0; left: 5px;
    border-left: 1px solid var(--line);
  }
  .dim-v__label {
    position: absolute; left: -16px; top: 50%;
    transform: translate(-50%, -50%) rotate(-90deg);
    font-size: 10px; white-space: nowrap;
  }

  .u36  { top: 172px; --w: 213px; --h: 74px; }
  .u42  { top: 346px; --w: 247px; --h: 72px; }
  .u50  { top: 537px; --w: 296px; --h: 82px; }
  .u72  { top: 740px; --w: 426px; --h: 87px; }
  .u100 { top: 929px; --w: 591px; --h: 97px; }

  /* Footer badge */
  .badge {
    position: absolute; left: 340px; top: 1120px;
    width: 64px; height: 58px;
    background: var(--header);
    border-radius: 4px;
  }
</style>
</head>
<body>
  <header class="header">
    <h1 class="header__title">DIMENSION</h1>
    <div class="brand">
      <span class="brand__mark"></span>
      <span class="brand__name">Tolvik<br>Hearthline</span>
    </div>
  </header>
  <svg class="header__stripes" viewBox="0 0 745 18" aria-hidden="true">
    <rect x="0" y="0" width="745" height="3" fill="#1b1c1e"/>
    <polygon points="0,4 260,4 248,9 0,9" fill="#f5b000"/>
    <polygon points="270,4 330,4 318,9 258,9" fill="#e08a00"/>
    <rect x="0" y="12" width="190" height="2" fill="#f5b000"/>
    <rect x="520" y="4" width="225" height="2" fill="#9a9a9a"/>
  </svg>

  <section class="unit u36">
    <div class="unit__size">36''</div>
    <div class="unit__frame"><div class="unit__flame" role="img" aria-label="Electric fireplace flame photo, 36 inch model"></div></div>
    <div class="dim-v"><span class="dim-v__label">430 mm</span></div>
    <div class="dim-h"><span class="dim-h__label">914 mm</span></div>
  </section>

  <section class="unit u42">
    <div class="unit__size">42''</div>
    <div class="unit__frame"><div class="unit__flame" role="img" aria-label="Electric fireplace flame photo, 42 inch model"></div></div>
    <div class="dim-v"><span class="dim-v__label">430 mm</span></div>
    <div class="dim-h"><span class="dim-h__label">1060 mm</span></div>
  </section>

  <section class="unit u50">
    <div class="unit__size">50''</div>
    <div class="unit__frame"><div class="unit__flame" role="img" aria-label="Electric fireplace flame photo, 50 inch model"></div></div>
    <div class="dim-v"><span class="dim-v__label">430 mm</span></div>
    <div class="dim-h"><span class="dim-h__label">1270 mm</span></div>
  </section>

  <section class="unit u72">
    <div class="unit__size">72''</div>
    <div class="unit__frame"><div class="unit__flame" role="img" aria-label="Electric fireplace flame photo, 72 inch model"></div></div>
    <div class="dim-v"><span class="dim-v__label">430 mm</span></div>
    <div class="dim-h"><span class="dim-h__label">1829 mm</span></div>
  </section>

  <section class="unit u100">
    <div class="unit__size">100''</div>
    <div class="unit__frame"><div class="unit__flame" role="img" aria-label="Electric fireplace flame photo, 100 inch model"></div></div>
    <div class="dim-v"><span class="dim-v__label">430 mm</span></div>
    <div class="dim-h"><span class="dim-h__label">2540 mm</span></div>
  </section>

  <div class="badge" aria-hidden="true"></div>
</body>
</html>
```